Business Profile Landing Page for search engine Start UP " Ember Gate"

Hi there
Ember Gate is an search engine for the Ember Gate - business.

What i´m looking for is a stunning singel Profile Landing Page for the Companys presentation.

Following Details should be included.

1st section
Comapanys name
Adress
info row ( opening time or what ever)
Profile Picture Big ( Could be the logo)
+3 smaller Pictures ( Maybe the store, main product ...)

2nd Section
navigation Icons for:
Call, Mail , Web, Route, Data

3er Section
About us.

Text lines.....
+Pictures slider

4th Section
1 row : Products ( Titel , Picture, Price)
2nd row :Service ( same as Products + text lines )

5th section
Blog Posts row

.....................................................
Well thats all, Colors used from the logo, u can also use the favicon somewhere (the crown magnifying glass)

Target Market(s)

All Comapnys, it should be an " used for all" design

Number of Pages Required

1 page

Requirements
Must have
• The first sighting is the important part, so the " first section should be impressively and makes the customers curious about more informations (very important for mobile version)
Nice to have
• If you can insert our favicon somewhere would be cool, but its not nessesery
Should not have
• you dont need to make a header or footer, that part is already done. i just need the main section design

```html
<!DOCTYPE html>
<html lang="en">
<head>
<meta charset="utf-8">
<title>Ember Gate – Business Profile</title>
<link rel="stylesheet" href="https://fonts.googleapis.com/css2?family=Raleway:wght@400;500;600;700&display=swap">
<style>
:root{
  --gold:#d4ae36;
  --gold-dark:#c99a1c;
  --navy:#1f5796;
  --ink:#2b2b2b;
  --text:#4a4a4a;
  --muted:#6b6b6b;
  --cream:#fdf9ef;
  --line:#d8d8d8;
  --white:#ffffff;
}
*{margin:0;padding:0;box-sizing:border-box}
html,body{width:1200px;height:2462px;overflow:hidden}
body{position:relative;font-family:"Raleway",sans-serif;color:var(--text);background:var(--white)}
.abs{position:absolute}

/* header */
.site-header{top:0;left:0;width:1200px;height:75px;border-bottom:1px solid #ececec}
.brand{left:152px;top:22px;display:flex;align-items:center;gap:6px}
.brand-mark{width:10px;height:10px;border-radius:50%;background:var(--gold-dark)}
.brand-name{font-weight:700;font-size:16px;color:var(--gold-dark);line-height:1}
.brand-tag{left:152px;top:43px;font-size:10px;color:var(--ink);font-weight:500}
.header-mail{right:152px;top:30px;display:flex;align-items:center;gap:8px;font-size:12px;color:var(--muted)}

/* hero */
.hero{top:75px;left:0;width:1200px;height:525px;
  background:linear-gradient(90deg,#f1e9dc 0%,#e8dccb 35%,#b9a58c 60%,#6f5a46 80%,#3f3128 100%)}
.hero-wash{top:0;left:0;width:700px;height:525px;background:linear-gradient(90deg,rgba(255,250,240,.75),rgba(255,250,240,0))}
.hero-title{left:153px;top:148px;font-size:38px;font-weight:700;color:#3a3a3a}
.hero-text{left:153px;top:208px;width:360px;font-size:13.5px;line-height:22.5px;color:#4d4d4d}
.btn{display:flex;align-items:center;justify-content:center;color:var(--white);font-size:11px;font-weight:500}
.btn-pill{background:var(--navy);border-radius:16px}
.hero-btn{left:152px;top:331px;width:150px;height:30px}

/* quick nav */
.quick-nav{top:600px;left:0;width:1200px;height:74px;background:var(--gold);display:flex}
.quick-item{display:flex;align-items:center;justify-content:center;gap:8px;color:var(--white);font-weight:600;font-size:13.5px;border-right:1px solid rgba(255,255,255,.25)}
.quick-item:last-child{border-right:none}

/* about */
.about-photo{left:151px;top:734px;width:375px;height:300px;background:linear-gradient(135deg,#4a4a3c 0%,#6c6854 45%,#2e3a34 75%,#4fa7a0 100%)}
.section-title{font-size:22px;font-weight:600;color:var(--ink)}
.about-title{left:611px;top:758px}
.about-text{left:611px;top:804px;width:425px;font-size:13.5px;line-height:22.5px;color:#4d4d4d}
.about-btn{left:612px;top:976px;width:151px;height:30px}

/* products */
.products-title{top:1089px;left:0;width:1200px;text-align:center}
.product-card{top:1158px;width:180px;height:259px;background:var(--white);box-shadow:2px 2px 3px rgba(0,0,0,.18)}
.product-photo{position:absolute;left:12px;top:9px;width:156px;height:150px;background:linear-gradient(135deg,#e8e8e6 0%,#c9c6c2 45%,#8a7d76 75%,#d9d4cf 100%)}
.product-name{position:absolute;top:180px;width:100%;text-align:center;font-size:15px;color:var(--ink);font-weight:500}
.product-rule{position:absolute;top:212px;left:72px;width:36px;height:1px;background:#555}
.product-price{position:absolute;top:226px;width:100%;text-align:center;font-size:15px;color:var(--ink);font-weight:600}
.all-products{left:450px;top:1462px;width:300px;height:29px;background:var(--gold);color:#2b2b2b;font-size:9.5px;font-weight:700}

/* services */
.services{top:1550px;left:0;width:1200px;height:392px;background:var(--cream)}
.services-title{top:1583px;left:0;width:1165px;text-align:center}
.service{top:1640px;width:210px;text-align:center}
.service svg{display:block;margin:0 auto;height:70px}
.service-name{margin-top:24px;font-size:15px;font-weight:500;color:var(--ink)}
.service-text{margin-top:14px;font-size:11.5px;line-height:18px;color:var(--muted)}
.services-btn{left:525px;top:1874px;width:150px;height:30px;font-weight:700;font-size:10px}

/* blogs */
.blogs-title{top:1995px;left:0;width:1175px;text-align:center}
.blog-card{width:413px;height:150px;border:1px solid #8a8a8a;background:var(--white)}
.blog-photo{position:absolute;left:0;top:0;width:150px;height:148px}
.photo-lens{background:linear-gradient(135deg,#6e6e6a 0%,#8c7a6c 50%,#4b4440 100%)}
.photo-puzzle{background:linear-gradient(135deg,#8b6a4a 0%,#b88d62 45%,#5a8fa6 70%,#7a5a40 100%)}
.blog-body{position:absolute;left:171px;top:28px;width:220px}
.blog-title{font-size:15px;font-weight:500;color:var(--ink)}
.blog-date{margin-top:6px;font-size:8px;color:var(--muted)}
.blog-text{margin-top:8px;font-size:11.5px;line-height:18px;color:var(--muted)}

/* footer */
.site-footer{top:2424px;left:0;width:1200px;height:38px;background:var(--gold)}
.copyright{left:152px;top:12px;font-size:11.5px;color:var(--white)}
.social{right:152px;top:11px;display:flex;gap:15px}
.social span{width:14px;height:14px;border-radius:50%;background:var(--white)}
</style>
</head>
<body>

<header class="site-header abs">
  <div class="brand abs"><span class="brand-mark"></span><span class="brand-name">Ember Gate</span></div>
  <div class="brand-tag abs">Floristen &amp; Gärtner</div>
  <div class="header-mail abs">
    <svg width="16" height="11" viewBox="0 0 16 11"><rect x="0.5" y="0.5" width="15" height="10" fill="none" stroke="#d4ae36"/><path d="M0.5 0.5 8 6 15.5 0.5" fill="none" stroke="#d4ae36"/></svg>
    hello@embergate.example
  </div>
</header>

<section class="hero abs" role="img" aria-label="Smiling shop assistant in an apron working at a café counter">
  <div class="hero-wash abs"></div>
  <h1 class="hero-title abs">Search for the Best.</h1>
  <p class="hero-text abs">Lorem ipsum dolor sit amet, consectetur adipiscing elit, sed do eiusmod tempor incididunt ut labore et dolore magna aliqua. Quis ipsum suspendisse ultrices gravida. Risus commodo viverra maecenas accumsan lacus vel.</p>
  <div class="hero-btn btn btn-pill abs">Learn more</div>
</section>

<nav class="quick-nav abs">
  <div class="quick-item" style="width:292px">
    <svg width="34" height="34" viewBox="0 0 34 34" fill="none" stroke="#fff" stroke-width="2"><path d="M7 3c-3 2-4 5-3 9 2 8 9 15 17 18 4 1 7 0 9-3l-5-5-4 3c-4-2-7-5-9-9l3-4z"/><path d="M20 4a10 10 0 0 1 10 10M20 9a5 5 0 0 1 5 5"/></svg>CALL</div>
  <div class="quick-item" style="width:206px">
    <svg width="44" height="32" viewBox="0 0 44 32" fill="none" stroke="#fff" stroke-width="2"><rect x="1" y="1" width="42" height="30"/><path d="M1 1l21 17L43 1"/></svg>MAIL</div>
  <div class="quick-item" style="width:198px">
    <svg width="38" height="38" viewBox="0 0 38 38" fill="none" stroke="#fff" stroke-width="2"><circle cx="19" cy="19" r="17"/><ellipse cx="19" cy="19" rx="7" ry="17"/><path d="M2 19h34M5 10h28M5 28h28"/></svg>WEB</div>
  <div class="quick-item" style="width:212px">
    <svg width="38" height="36" viewBox="0 0 38 36" fill="none" stroke="#fff" stroke-width="2"><path d="M30 16s-6-6-6-10a6 6 0 0 1 12 0c0 4-6 10-6 10z"/><circle cx="30" cy="6" r="2"/><path d="M8 34s-6-6-6-10a6 6 0 0 1 12 0c0 4-6 10-6 10z"/><circle cx="8" cy="24" r="2"/><path d="M12 32h10a4 4 0 0 0 0-8h-2a4 4 0 0 1 0-8h8"/></svg>ROUTE</div>
  <div class="quick-item" style="width:292px">
    <svg width="38" height="38" viewBox="0 0 38 38" fill="none" stroke="#fff" stroke-width="2"><rect x="1" y="1" width="36" height="10"/><rect x="1" y="14" width="36" height="10"/><rect x="1" y="27" width="36" height="10"/><path d="M6 6h8M6 19h8M6 32h8M28 6h4M28 19h4M28 32h4"/></svg>DATA</div>
</nav>

<div class="about-photo abs" role="img" aria-label="Smiling businessman with glasses working on a laptop"></div>
<h2 class="section-title about-title abs">About Us</h2>
<p class="about-text abs">Lorem ipsum dolor sit amet, consectetur adipiscing elit, sed do eiusmod tempor incididunt ut labore et dolore magna aliqua. Quis ipsum suspendisse ultrices gravida. Risus commodo viverra maecenas accumsan lacus vel facilisis. Lorem ipsum dolor sit amet, consectetur adipiscing elit, sed do eiusmod tempor incididunt ut labore et dolore magna aliqua. Quis ipsum suspendisse ultrices/</p>
<div class="about-btn btn btn-pill abs">Learn more</div>

<h2 class="section-title products-title abs">Our Products</h2>
<div class="product-card abs" style="left:153px"><div class="product-photo" role="img" aria-label="Hands typing on a laptop keyboard"></div><div class="product-name">Lorem Ipsum</div><div class="product-rule"></div><div class="product-price">$150</div></div>
<div class="product-card abs" style="left:392px"><div class="product-photo" role="img" aria-label="Hands typing on a laptop keyboard"></div><div class="product-name">Lorem Ipsum</div><div class="product-rule"></div><div class="product-price">$150</div></div>
<div class="product-card abs" style="left:630px"><div class="product-photo" role="img" aria-label="Hands typing on a laptop keyboard"></div><div class="product-name">Lorem Ipsum</div><div class="product-rule"></div><div class="product-price">$150</div></div>
<div class="product-card abs" style="left:869px"><div class="product-photo" role="img" aria-label="Hands typing on a laptop keyboard"></div><div class="product-name">Lorem Ipsum</div><div class="product-rule"></div><div class="product-price">$150</div></div>
<div class="all-products btn abs">SEE ALL PRODUCTS</div>

<section class="services abs"></section>
<h2 class="section-title services-title abs">Our Services</h2>
<div class="service abs" style="left:150px">
  <svg viewBox="0 0 80 70" fill="none" stroke="#222" stroke-width="2"><path d="M2 68h76"/><rect x="12" y="50" width="8" height="18"/><rect x="26" y="42" width="8" height="26"/><rect x="40" y="34" width="8" height="34"/><rect x="54" y="26" width="8" height="42"/><path d="M8 40 L30 26 40 30 66 6"/><path d="M56 6h10v10"/></svg>
  <div class="service-name">Reputation Management</div>
  <p class="service-text">Lorem ipsum dolor sit amet, consectetur adipiscing elit, sed do eiusmod tempor incididunt ut labore et dolore magna aliqua.</p>
</div>
<div class="service abs" style="left:380px">
  <svg viewBox="0 0 80 70" fill="none" stroke="#222" stroke-width="2"><rect x="2" y="8" width="70" height="56"/><path d="M72 8V2h6v62h-6"/><rect x="30" y="28" width="16" height="14"/><rect x="12" y="18" width="10" height="8"/><rect x="54" y="18" width="10" height="8"/><rect x="12" y="46" width="10" height="8"/><rect x="54" y="46" width="10" height="8"/><path d="M22 22h8v8M54 22h-8v6M22 50h8v-8M54 50h-8v-8"/></svg>
  <div class="service-name">Branding &amp; Presence</div>
  <p class="service-text">Lorem ipsum dolor sit amet, consectetur adipiscing elit, sed do eiusmod tempor incididunt ut labore et dolore magna aliqua.</p>
</div>
<div class="service abs" style="left:610px">
  <svg viewBox="0 0 80 70" fill="none" stroke="#222" stroke-width="2"><path d="M10 2h34l10 10v56H10z"/><rect x="16" y="16" width="6" height="6"/><rect x="16" y="30" width="6" height="6"/><rect x="16" y="44" width="6" height="6"/><path d="M26 19h10M26 33h6M26 47h6"/><circle cx="50" cy="42" r="12"/><path d="M44 42l4 4 8-8M59 51l12 12"/></svg>
  <div class="service-name">Business Listing</div>
  <p class="service-text">Lorem ipsum dolor sit amet, consectetur adipiscing elit, sed do eiusmod tempor incididunt ut labore et dolore magna aliqua.</p>
</div>
<div class="service abs" style="left:840px;top:1637px">
  <svg viewBox="0 0 80 70" fill="none" stroke="#222" stroke-width="2"><rect x="2" y="14" width="10" height="28"/><rect x="68" y="14" width="10" height="28"/><path d="M12 18h14l10-4 10 6-12 6M68 18H54l-12 8 12 14M12 38l6 2 6 6 4-2 4 6 4-2 4 4 6-6"/></svg>
  <div class="service-name">Business Suite</div>
  <p class="service-text">Lorem ipsum dolor sit amet, consectetur adipiscing elit, sed do eiusmod tempor incididunt ut labore et dolore magna aliqua.</p>
</div>
<div class="services-btn btn btn-pill abs">LEAR MORE</div>

<h2 class="section-title blogs-title abs">Latest Blogs</h2>
<article class="blog-card abs" style="left:152px;top:2045px"><div class="blog-photo photo-lens" role="img" aria-label="Woman looking through a magnifying glass"></div><div class="blog-body"><h3 class="blog-title">Stream Flame</h3><div class="blog-date">2020 July 10</div><p class="blog-text">Lorem ipsum dolor sit amet, consectetur adipiscing elit, sed do eiusmod tempor incididunt [...]</p></div></article>
<article class="blog-card abs" style="left:635px;top:2045px"><div class="blog-photo photo-puzzle" role="img" aria-label="Team hands joining colourful puzzle pieces on a wooden table"></div><div class="blog-body"><h3 class="blog-title">Stream Flame</h3><div class="blog-date">2020 July 10</div><p class="blog-text">Lorem ipsum dolor sit amet, consectetur adipiscing elit, sed do eiusmod tempor incididunt [...]</p></div></article>
<article class="blog-card abs" style="left:153px;top:2210px"><div class="blog-photo photo-puzzle" role="img" aria-label="Team hands joining colourful puzzle pieces on a wooden table"></div><div class="blog-body"><h3 class="blog-title">Stream Flame</h3><div class="blog-date">2020 July 10</div><p class="blog-text">Lorem ipsum dolor sit amet, consectetur adipiscing elit, sed do eiusmod tempor incididunt [...]</p></div></article>
<article class="blog-card abs" style="left:636px;top:2210px"><div class="blog-photo photo-lens" role="img" aria-label="Woman looking through a magnifying glass"></div><div class="blog-body"><h3 class="blog-title">Stream Flame</h3><div class="blog-date">2020 July 10</div><p class="blog-text">Lorem ipsum dolor sit amet, consectetur adipiscing elit, sed do eiusmod tempor incididunt [...]</p></div></article>

<footer class="site-footer abs">
  <div class="copyright abs">Copyright © 2020 Ember Gate</div>
  <div class="social abs"><span></span><span></span><span></span><span></span><span></span></div>
</footer>

</body>
</html>
```